Flyer Design for Non-Profit working with people with mental disabilities

We are Harbor Pathways, a non profit working with people with disabilities and helping them to live the best life they can.

We need a modern pamphlet designed for our service offerings. We don't want a single completed pamphlet, but 2 templates which we can then add our own photos and text to. We need:
*One double sided 210mm x 100mm template in portrait orientation
*One double sided 210mm x 200mm folded template in portrait orientation

The pamphlets need to be bold, happy, concise and easy to understand.

As for the content which we will add later we need room on both the front and back of the flier to add photos and text in later similar to the 5 Lanterns pamphlet.

As for the other flyer designs I uploaded, I like their simple, bold designs.

Also I uploaded a Harbor Works logo as well. I would like the logos to be switched out for a second copy of the templates with the different logo.
Updates

So just so everyone's on the same page here. I want to use this as a template for multiple separate services. I want a section on the front page for a pictures which I can change to suit the service, room for a clear title, and a paragraph of text. Refer to the 5 lanterns example to get an idea of what I'm looking for. On the back I was room for text. Don't worry about the photos I uploaded, I don't actually want photos with alpha backgrounds on the flyer, they were for one of the designers to use but I didn't like it. Just use stock photos of happy people for now. Again refer to the 5 lanterns example of how they're photos were set out. Thanks.

Target Market(s)

The families and carers of people with disabilities

Industry/Entity Type

Non Profit

Font styles to use
Other font styles liked:
• Museo Sans 300 and Museo Sans 500

Requirements
Must have
• The Harbor Pathways logo
• And our tagline: We listen, We plan, We do, We care
Nice to have
• A colour scheme which ties in well with our logo

```html
<!DOCTYPE html>
<html lang="en">
<head>
<meta charset="utf-8">
<title>Harbor Works – Service Flyer</title>
<link rel="stylesheet" href="https://fonts.googleapis.com/css2?family=Lato:wght@400;700;900&display=swap">
<style>
  :root{
    --orange:#f28a12;
    --orange-deep:#e4740a;
    --blue:#4a6fb5;
    --blue-soft:#8fa6d6;
    --sky-top:#6f9fd4;
    --sky-low:#dce8f4;
    --warm-photo:#c98a5a;
    --ink:#2f3340;
    --white:#ffffff;
  }
  *{margin:0;padding:0;box-sizing:border-box}
  html,body{width:791px;height:1200px;overflow:hidden;background:#f2f2f2}
  .flyer{position:relative;width:791px;height:1200px;background:var(--white);overflow:hidden;font-family:'Lato',sans-serif}

  .hero-photo{position:absolute;left:0;top:0;width:791px;height:600px;
    background:linear-gradient(180deg,var(--sky-top) 0%,#9cbbe2 45%,#d9b08a 78%,var(--warm-photo) 100%)}

  .brand{position:absolute;right:40px;top:56px;display:flex;flex-direction:column;align-items:flex-end;gap:8px}
  .brand-row{display:flex;align-items:center;gap:14px}
  .brand-dot{width:46px;height:46px;border-radius:50%;background:var(--orange)}
  .brand-name{font-weight:900;font-size:34px;line-height:1;color:var(--blue);text-transform:uppercase;letter-spacing:.5px}
  .tagline{font-weight:700;font-size:16px;line-height:1;color:var(--blue);letter-spacing:.3px}

  .swoosh{position:absolute;left:0;top:330px;width:791px;height:330px}

  .info-panel{position:absolute;left:0;top:560px;width:520px;height:520px;background:linear-gradient(180deg,var(--orange),var(--orange-deep))}
  .headline{position:absolute;left:36px;top:612px;width:470px;color:var(--white);font-weight:900;font-size:50px;line-height:1.08;text-transform:uppercase}
  .lead{position:absolute;left:36px;top:742px;width:450px;color:var(--white);font-size:19px;line-height:1.35}

  .side-photo{position:absolute;left:520px;top:720px;width:271px;height:480px;
    background:linear-gradient(180deg,#7aa5d8 0%,#bcd2ec 45%,#e9a25a 72%,var(--orange-deep) 100%)}

  .call-badge{position:absolute;left:70px;top:930px;width:200px;height:200px;border-radius:50%;background:var(--white);
    border:8px solid var(--blue-soft);display:flex;flex-direction:column;align-items:center;justify-content:center;text-transform:uppercase;font-weight:900;line-height:1}
  .call-badge .small{font-size:36px;color:var(--ink)}
  .call-badge .big{font-size:54px;color:var(--orange)}

  .contact{position:absolute;left:40px;top:1142px;display:flex;align-items:center;gap:14px;color:var(--ink);font-size:36px;font-weight:700;line-height:1}
  .contact svg{width:32px;height:32px}
</style>
</head>
<body>
<main class="flyer">
  <div class="hero-photo" role="img" aria-label="Photo of a smiling young woman in an orange safety vest against a blue sky"></div>

  <div class="brand">
    <div class="brand-row">
      <span class="brand-dot"></span>
      <span class="brand-name">Harbor Works</span>
    </div>
    <span class="tagline">We listen, We plan, We do, We care</span>
  </div>

  <svg class="swoosh" viewBox="0 0 791 330" preserveAspectRatio="none" aria-hidden="true">
    <path d="M0 230 C220 170 480 120 791 0 L791 330 L0 330 Z" fill="#ffffff"/>
    <path d="M0 230 C220 170 480 120 791 0" fill="none" stroke="#4a6fb5" stroke-width="10"/>
    <path d="M0 252 C230 195 500 150 791 40" fill="none" stroke="#8fa6d6" stroke-width="5"/>
  </svg>

  <div class="info-panel"></div>
  <h1 class="headline">Lorem ipsum<br>dolor sit amet</h1>
  <p class="lead">Lorem ipsum dolor sit amet, ad tacimates intellegam scripserit mea, te quo vitae civibus prodesset. At per saperet in has mutat integre vulputate. Et quas possim adversarium mei, veri magna iracundia ei est. Tale eum aliqui lucilius neglegentur, ut quando apeirian accommodare pro.</p>

  <div class="side-photo" role="img" aria-label="Photo of a smiling young man in an orange safety vest against a blue sky"></div>

  <div class="call-badge">
    <span class="small">Call us</span>
    <span class="big">Now</span>
  </div>

  <div class="contact">
    <svg viewBox="0 0 24 24" aria-hidden="true"><rect x="1" y="1" width="22" height="22" rx="4" fill="#4a6fb5"/><path d="M8 5.5l2 2.5-1.3 1.6c.8 1.8 2 3 3.8 3.8l1.6-1.3 2.5 2-1.2 2.4c-4.8-.4-8.9-4.5-9.3-9.3z" fill="#fff"/></svg>
    <span class="phone">123 456 7890</span>
  </div>
</main>
</body>
</html>
```